Illustrations for women's leadership website

Bright Lanterns Consulting is a coaching and consulting firm that helps women work through transition in all areas of their lives - marriage and divorce, job promotions and management, health and wellness, sexuality and power - to create their best, happiest lives. We believe that life is messy - women are constantly trying to juggle multiple projects and tasks, we are always negotiating with our husbands and lovers, our kids, our bosses and employees and ourselves, and life is always moving and changing around us. We help women of all ages cut through the mess and focus on what's really important to them in order to enjoy the journey - and the mess - that is life.

Our web site is under development and we would like some unique illustrations to represent our personality. Bright Lanterns Consulting is a team - Rosalind and Margot - along with our network of contacts and honorary "bright lanterns" we bring in to support women with their various challenges. We are direct but tactful. We help women uncover their strengths and their own personal power. We like to have fun. We believe in living your life, not letting it drag you along through the undertow. We believe we all have the power to enjoy our lives, even the messy parts, when we have faith in who we are and what gifts we bring to the world.

Our key values:
- Passion
- Honesty
- Fun
- Wisdom
- Health

We'd like the illustrations to focus on women, in activities that give them happiness and power (out with friends, spending time by themselves, listening to music or exercising, at work). The name Bright Lanterns was established because one of the things Margot and I do to relax and have fun is run obstacle course races, where you get very muddy and dirty! But also work your body hard and accomplish challenging physical goals.

We'd like to develop a set of images - four or five that we can use on our site - but will start with this first one. Once we find a design/style we like, we will continue to work with you to develop the additional images we need. We'd like to start with an image for our home page - a banner image, essentially (see www.brightlanternsconsulting.example) that will represent us and be the first thing our clients see.

I am attaching our logo, so you can see the one element we are committed to working with. You can go to our website, www.brightlanternsconsulting.example, to see how it's under development and to see our blog page. I am also attaching a couple photos of myself and my partner Margot, which you may use our likeness in your illustrations. I am also attaching a couple of illustrative images we kind of like - but we're not saying your work has to look like this. It's just to provide a little style guidance.

We do not want anything too "cartoon" looking. We're a professional firm and want to look professional but at the same time offer an accessible, fun style that encourages women to open up to us, to trust us and know we understand just how messy life is and we can help them negotiate it.

Please contact me with any questions for clarification. I know this can seem a challenging project.
Updates

Project Deadline Extended
Reason: We need a design that fits a home page banner. Some of the illustrations we received have potential from a style perspective, but they don't fit a home page banner for a women's leadership site. Please reference www.brightlanternsconsulting.example - you can see the current state of the web site and how we need a banner!

Target Market(s)

Women, ages 22-75.

Industry/Entity Type

Life Coaching

Requirements
Must have
• Personable but professional, sophisticated but fun. Should feature women.
Nice to have
• could feature women that look like me and Margot, (brunette and blond, ages 40s and 50s).
Should not have
• Not too 'cartoon' looking.

```html
<!DOCTYPE html>
<html lang="en">
<head>
<meta charset="utf-8">
<title>Bright Lanterns Consulting — Home</title>
<link href="https://fonts.googleapis.com/css2?family=Open+Sans:wght@400;600;700&family=Roboto+Condensed:wght@400;700&display=swap" rel="stylesheet">
<style>
  :root {
    --brand-red: #c52d2f;
    --brand-coral: #e8756a;
    --brand-peach: #f3a08c;
    --ink: #3a3a3a;
    --nav-ink: #444;
    --band-grey: #f5f5f5;
    --footer-bg: #3c3f44;
    --footer-ink: #ffffff;
    --rule: #dddddd;
    --button-grey: #9b9b9b;
    --white: #ffffff;
    --portrait-light: #f4d2a6;
    --portrait-light-edge: #eab08f;
    --portrait-dark: #5c4038;
    --portrait-dark-edge: #e39a86;
  }
  * { box-sizing: border-box; margin: 0; padding: 0; }
  html, body { width: 1200px; height: 750px; overflow: hidden; background: var(--white); }
  body { position: relative; font-family: "Open Sans", Arial, sans-serif; color: var(--ink); }

  .site-header { position: absolute; inset: 0 0 auto 0; height: 210px; }
  .brand { position: absolute; left: 152px; top: 112px; display: flex; align-items: center; gap: 12px; }
  .brand-square { width: 46px; height: 46px; background: var(--brand-red); }
  .brand-name { font-size: 24px; font-weight: 700; color: var(--brand-red); letter-spacing: -0.2px; }

  .main-nav { position: absolute; top: 71px; left: 704px; display: flex; height: 137px; }
  .main-nav a { display: flex; align-items: center; font-size: 11px; font-weight: 700; color: var(--nav-ink); text-decoration: none; text-transform: uppercase; letter-spacing: 0.3px; }
  .main-nav .nav-home { width: 67px; justify-content: center; background: var(--brand-red); color: var(--white); }
  .main-nav .nav-services { margin-left: 17px; }
  .main-nav .nav-about { margin-left: 34px; }
  .main-nav .nav-blog { margin-left: 34px; }
  .main-nav .nav-contact { margin-left: 35px; }

  .page-title-band { position: absolute; top: 210px; left: 0; width: 1200px; height: 78px; background: var(--band-grey); }
  .page-title { position: absolute; left: 142px; top: 29px; font-size: 17px; font-weight: 400; letter-spacing: 2.5px; color: var(--ink); }

  .hero-banner { position: absolute; top: 288px; left: 0; width: 1200px; height: 154px; border-top: 2px solid var(--brand-red); border-bottom: 2px solid var(--brand-red);
    background: linear-gradient(90deg, #d9433f 0%, #e3625a 35%, #e7786b 55%, #e1655a 75%, #ec9384 100%); overflow: hidden; }

  .hero-backdrop { position: absolute; top: 0; height: 150px; }
  .hero-backdrop--left { left: 440px; width: 190px;
    background: linear-gradient(90deg, rgba(240,160,140,0) 0%, rgba(242,170,150,0.7) 55%, rgba(240,160,140,0.2) 100%); }
  .hero-backdrop--right { left: 1000px; width: 200px;
    background: linear-gradient(90deg, rgba(240,160,140,0) 0%, rgba(246,185,168,0.75) 50%, rgba(244,175,160,0.6) 100%); }

  .hero-portrait { position: absolute; top: 4px; height: 146px; border-radius: 70px 70px 0 0; }
  .hero-portrait--blonde { left: 636px; width: 138px;
    background: linear-gradient(180deg, var(--portrait-light) 0%, #f1c49e 55%, var(--portrait-light-edge) 100%); }
  .hero-portrait--brunette { left: 826px; width: 124px;
    background: linear-gradient(180deg, var(--portrait-dark) 0%, #8a5c4e 35%, var(--portrait-dark-edge) 100%); }

  .hero-copy { position: absolute; left: 6px; top: 10px; font-family: "Roboto Condensed", "Arial Narrow", sans-serif; font-weight: 700; font-size: 18px; line-height: 27px; color: var(--white); letter-spacing: -0.3px; }
  .hero-copy .indent { padding-left: 11px; }
  .hero-values { position: absolute; left: 965px; top: 6px; font-family: "Roboto Condensed", "Arial Narrow", sans-serif; font-weight: 700; font-size: 18px; line-height: 23.5px; color: var(--white); list-style: none; }

  .site-footer { position: absolute; top: 470px; left: 0; width: 1200px; height: 82px; background: var(--footer-bg); border-top: 2px solid var(--brand-red);
    color: var(--footer-ink); text-align: center; font-size: 12px; line-height: 19px; padding-top: 27px; }

  .page-end-rule { position: absolute; top: 680px; left: 0; width: 1200px; height: 2px; background: var(--rule); }
  .contact-button { position: absolute; left: 1154px; top: 630px; width: 38px; height: 38px; background: var(--button-grey); display: flex; align-items: center; justify-content: center; }
</style>
</head>
<body>
  <header class="site-header">
    <div class="brand">
      <span class="brand-square"></span>
      <span class="brand-name">Bright Lanterns Consulting</span>
    </div>
    <nav class="main-nav">
      <a class="nav-home" href="#">Home</a>
      <a class="nav-services" href="#">Services</a>
      <a class="nav-about" href="#">About</a>
      <a class="nav-blog" href="#">Blog</a>
      <a class="nav-contact" href="#">Contact</a>
    </nav>
  </header>

  <section class="page-title-band">
    <h1 class="page-title">HOME</h1>
  </section>

  <section class="hero-banner">
    <div class="hero-backdrop hero-backdrop--left" role="img" aria-label="Large faded painted portrait of a smiling woman blended into the coral background"></div>
    <div class="hero-backdrop hero-backdrop--right" role="img" aria-label="Large faded painted portrait of a smiling woman with light lines sweeping across the coral background"></div>
    <div class="hero-portrait hero-portrait--blonde" role="img" aria-label="Painted portrait of Rosalind, a smiling woman with long blonde hair"></div>
    <div class="hero-portrait hero-portrait--brunette" role="img" aria-label="Painted portrait of Margot, a smiling woman with short dark brown hair"></div>
    <p class="hero-copy">
      Bright Lanterns Consulting is a coaching and consulting firm that helps<br>
      <span class="indent">women work through transition in all areas of their lives -</span><br>
      marriage and divorce, job promotions and management,<br>
      <span class="indent">health and wellnes, sexuality and power - to create</span><br>
      their best, happiest lives.
    </p>
    <ul class="hero-values">
      <li>Our key values:</li>
      <li>Passion</li>
      <li>Honesty</li>
      <li>Fun</li>
      <li>Wisdom</li>
      <li>Health</li>
    </ul>
  </section>

  <footer class="site-footer">
    <p>© BRIGHT LANTERNS CONSULTING 2015</p>
    <p>Designed and Developed by Northfield Studio</p>
  </footer>

  <div class="page-end-rule"></div>

  <a class="contact-button" href="#" aria-label="Send a message">
    <svg width="20" height="15" viewBox="0 0 20 15" aria-hidden="true">
      <path d="M0 0h20v1.5L10 8 0 1.5z" fill="#fff"/>
      <path d="M0 3.5l10 6.5 10-6.5V15H0z" fill="#fff"/>
    </svg>
  </a>
</body>
</html>
```